Business Cards for 41Vale

I need business cards that goes with the logo
Updates

Dear designers - many thanks for the responsesreceived to date. There are many good designs but most of them are landscape.Could you please submit a few options for portrait layout as well.

Industry/Entity Type

Business

```html
<!DOCTYPE html>
<html lang="en">
<head>
<meta charset="utf-8">
<title>41Vale Business Card</title>
<link rel="stylesheet" href="https://fonts.googleapis.com/css2?family=Michroma&family=Questrial&family=Cormorant+Garamond:wght@500&family=Montserrat:wght@700&display=swap">
<style>
  :root {
    --stage-top: #c7c6c7;
    --stage-bottom: #ebebeb;
    --red-deep: #3d0002;
    --red-mid: #6e0004;
    --red-bright: #9c0006;
    --brand-red: #8e1016;
    --ink: #2b2b2b;
    --grey-mark: #5d6166;
    --paper: #ffffff;
    --paper-shade: #e6e6e6;
    --label: #3a3a3a;
  }
  * { margin: 0; padding: 0; box-sizing: border-box; }
  html, body { width: 1200px; height: 765px; overflow: hidden; }
  body {
    position: relative;
    background: linear-gradient(180deg, var(--stage-top) 0%, #d6d5d6 40%, var(--stage-bottom) 75%, #dcdcdc 100%);
    font-family: "Questrial", sans-serif;
  }
  .card {
    position: absolute;
    top: 302px;
    width: 575px;
    height: 344px;
    border-radius: 40px;
    overflow: hidden;
    box-shadow: 0 14px 22px rgba(0,0,0,0.22);
  }
  .card--front {
    left: 16px;
    background: linear-gradient(180deg, var(--red-deep) 0%, var(--red-mid) 45%, var(--red-bright) 100%);
  }
  .card--back {
    left: 604px;
    background: linear-gradient(160deg, var(--paper) 0%, #f1f1f1 50%, var(--paper-shade) 100%);
    border: 1px solid #d2d2d2;
  }
  .logo-panel {
    position: absolute;
    left: 275px;
    top: 161px;
    width: 300px;
    height: 119px;
    background: var(--paper);
    border-top: 6px solid var(--grey-mark);
    box-shadow: -4px 10px 16px rgba(0,0,0,0.35);
    display: flex;
    align-items: center;
    padding-left: 10px;
    gap: 10px;
  }
  .brand-dot {
    width: 16px; height: 16px; border-radius: 50%;
    background: var(--brand-red);
  }
  .brand-name {
    font-family: "Montserrat", sans-serif;
    font-weight: 700;
    font-size: 42px;
    color: var(--brand-red);
    letter-spacing: -0.5px;
  }
  .name-band {
    position: absolute;
    left: 0;
    top: 167px;
    width: 300px;
    height: 112px;
    background: linear-gradient(180deg, #7a0006 0%, var(--red-bright) 100%);
    border-radius: 0 6px 6px 0;
    box-shadow: 0 12px 18px rgba(0,0,0,0.35);
    text-align: right;
    padding: 27px 13px 0 0;
    color: var(--paper);
  }
  .person-name {
    font-family: "Michroma", sans-serif;
    font-size: 24px;
    line-height: 1.1;
    letter-spacing: -0.5px;
  }
  .person-title {
    font-family: "Questrial", sans-serif;
    font-size: 11.5px;
    letter-spacing: 0.4px;
    margin-top: 4px;
  }
  .mini-brand {
    position: absolute;
    right: 34px;
    top: 40px;
    display: flex;
    align-items: center;
    gap: 5px;
  }
  .mini-brand .brand-dot { width: 8px; height: 8px; }
  .mini-brand .brand-name { font-size: 17px; }
  .contact-list {
    position: absolute;
    right: 16px;
    top: 176px;
    list-style: none;
  }
  .contact-list li {
    display: flex;
    justify-content: flex-end;
    align-items: center;
    gap: 12px;
    height: 19.5px;
    font-size: 13px;
    color: var(--ink);
    letter-spacing: 0.3px;
  }
  .contact-list svg { width: 15px; height: 15px; fill: var(--brand-red); flex: none; }
  .side-label {
    position: absolute;
    top: 684px;
    font-family: "Cormorant Garamond", serif;
    font-weight: 500;
    font-size: 15px;
    letter-spacing: 3px;
    color: var(--label);
  }
  .side-label--front { left: 66px; }
  .side-label--back { left: 659px; }
</style>
</head>
<body>
  <section class="card card--front" aria-label="Card front">
    <div class="logo-panel">
      <span class="brand-dot"></span>
      <span class="brand-name">41Vale</span>
    </div>
  </section>

  <section class="card card--back" aria-label="Card back">
    <div class="mini-brand">
      <span class="brand-dot"></span>
      <span class="brand-name">41Vale</span>
    </div>
    <div class="name-band">
      <div class="person-name">MARA LIND</div>
      <div class="person-title">EXECUTIVE VICE PRESIDENT</div>
    </div>
    <ul class="contact-list">
      <li>555.0142.310
        <svg viewBox="0 0 16 16" aria-hidden="true"><rect x="4" y="1" width="8" height="4"/><rect x="1" y="6" width="14" height="6" rx="1"/><rect x="4" y="10" width="8" height="5"/></svg>
      </li>
      <li>555.0142.311
        <svg viewBox="0 0 16 16" aria-hidden="true"><path d="M1 6c0-3 14-3 14 0v2h-4V6H5v2H1z"/><path d="M3 9h10l1 6H2z"/></svg>
      </li>
      <li>555.0142.312
        <svg viewBox="0 0 16 16" aria-hidden="true"><rect x="1" y="2" width="14" height="13" rx="1"/><rect x="3" y="4" width="10" height="3" fill="#fff"/><rect x="3" y="9" width="2" height="2" fill="#fff"/><rect x="7" y="9" width="2" height="2" fill="#fff"/><rect x="11" y="9" width="2" height="2" fill="#fff"/></svg>
      </li>
      <li>41vale.com
        <svg viewBox="0 0 16 16" aria-hidden="true"><path d="M8 1a7 7 0 1 0 4 12.7l-.9-1.3A5.4 5.4 0 1 1 13.4 8v.8c0 .8-.5 1.3-1.1 1.3s-1-.5-1-1.3V4.6H9.7v.6A3.3 3.3 0 1 0 10 10.6 2.6 2.6 0 0 0 15 8.8V8a7 7 0 0 0-7-7zm-.4 8.9a1.9 1.9 0 1 1 0-3.8 1.9 1.9 0 0 1 0 3.8z"/></svg>
      </li>
      <li>MaraLind@41vale.com
        <svg viewBox="0 0 16 16" aria-hidden="true"><path d="M1 6l7-4 7 4v8H1z"/><path d="M2 6.5l6 4 6-4" fill="none" stroke="#fff" stroke-width="1.2"/></svg>
      </li>
    </ul>
  </section>

  <p class="side-label side-label--front">FRONT</p>
  <p class="side-label side-label--back">BACK</p>
</body>
</html>
```